Velorak app icon design

We are building an Velorak app and would like some good looking icons to replace the boring ones we have created ourselves.

Please see attached screen shots.

The icons toggle "Active/Inactive" where the inactive is shaded out.

Building

```html
<!DOCTYPE html>
<html lang="en">
<head>
<meta charset="utf-8">
<title>Velorak – Search screens</title>
<link rel="stylesheet" href="https://fonts.googleapis.com/css2?family=Inter:wght@300;400;500;600&display=swap">
<style>
:root{
  --bg:#e9e9e9;
  --nav:#004a8f;
  --bar:#f7f7f7;
  --field-area:#efeff1;
  --line:#d4d4d6;
  --text:#8e8e93;
  --text-dark:#1b1b1b;
  --portfolio:#3a8ee6;
  --property:#f0434f;
  --owner:#e0b02a;
  --tenant:#74c920;
  --staff:#f2a61e;
  --kb:#d1d5db;
  --key:#ffffff;
  --key-special:#adb3bc;
  --key-shadow:#8a8d92;
  --go:#0a7cff;
}
*{box-sizing:border-box;margin:0;padding:0}
html,body{width:1200px;height:1000px;overflow:hidden}
body{background:var(--bg);font-family:"Inter",sans-serif;position:relative}
.screen{position:absolute;top:180px;width:334px;height:596px;background:#fff;overflow:hidden}
.screen--empty{left:236px}
.screen--results{left:666px}

.status{height:21px;background:var(--bar);display:flex;align-items:center;justify-content:space-between;padding:0 6px;font-size:12px;font-weight:500;color:var(--text-dark);position:relative}
.status__time{position:absolute;left:0;right:0;text-align:center}
.status__left,.status__right{display:flex;align-items:center;gap:4px}
.signal{display:flex;gap:1.5px}
.signal i{width:6px;height:6px;border-radius:50%;background:var(--text-dark);display:block}
.signal i.off{background:none;border:1px solid var(--text-dark)}
.battery{width:22px;height:10px;border:1px solid var(--text-dark);border-radius:2px;position:relative}
.battery::before{content:"";position:absolute;left:1px;top:1px;bottom:1px;width:3px;background:#e0222b}

.nav{height:46px;background:var(--nav);color:#fff;position:relative;display:flex;align-items:center}
.nav__back{display:flex;align-items:center;gap:6px;padding-left:9px;font-size:18px;font-weight:300}
.nav__title{position:absolute;left:0;right:0;text-align:center;font-size:20px;font-weight:600;pointer-events:none}

.tabs{height:58px;background:var(--bar);display:flex;border-bottom:1px solid var(--line)}
.tab{flex:1;display:flex;flex-direction:column;align-items:center;padding-top:7px;font-size:10px;color:var(--text)}
.tab svg{width:28px;height:28px;margin-bottom:5px}
.tab--active{color:var(--portfolio)}

.search{height:45px;background:var(--field-area);padding:8px 8px;border-bottom:1px solid var(--line)}
.search__field{height:29px;background:#fff;border-radius:5px;display:flex;align-items:center;padding:0 8px;gap:6px;font-size:14px;color:#a4a4a8}
.search__field .clear{margin-left:auto}

.results{height:198px;padding:0 14px 0 16px}
.row{height:46px;border-bottom:1px solid var(--line);display:flex;align-items:center;gap:14px}
.row__icon{width:28px;height:28px;flex:none;margin-left:12px}
.row__text{flex:1;font-size:14px;line-height:17px;color:var(--text);white-space:nowrap}
.row__chevron{flex:none;margin-right:16px}

.keyboard{position:absolute;left:0;right:0;bottom:0;height:228px;background:var(--kb);padding:14px 2px 0}
.keys{display:flex;gap:3.2px;height:38px;margin-bottom:18.5px}
.keys--home{padding-left:16px}
.keys--shift{justify-content:space-between}
.keys--shift .group{display:flex;gap:3.2px}
.key{width:30.5px;height:38px;background:var(--key);border-radius:5px;box-shadow:0 1px 0 var(--key-shadow);display:flex;align-items:center;justify-content:center;font-size:21px;font-weight:300;color:var(--text-dark)}
.key--special{background:var(--key-special)}
.key--wide{width:38px}
.key--num{width:36px;font-size:15px}
.key--globe{width:36px}
.key--mic{width:27px;background:var(--key)}
.key--space{width:78px;font-size:15px}
.key--com{width:42px;font-size:15px}
.key--go{width:77px;background:var(--go);color:#fff;font-size:16px}
.keys--bottom{gap:6px}
</style>
</head>
<body>

<svg width="0" height="0" style="position:absolute">
  <defs>
    <symbol id="ico-portfolio" viewBox="0 0 28 28">
      <rect x="6" y="2" width="17" height="24" rx="1.5" fill="var(--portfolio)"/>
      <g stroke="#1d5fa8" stroke-width="1.4">
        <line x1="5" y1="5" x2="8" y2="5"/><line x1="5" y1="8" x2="8" y2="8"/><line x1="5" y1="11" x2="8" y2="11"/>
        <line x1="5" y1="14" x2="8" y2="14"/><line x1="5" y1="17" x2="8" y2="17"/><line x1="5" y1="20" x2="8" y2="20"/><line x1="5" y1="23" x2="8" y2="23"/>
      </g>
    </symbol>
    <symbol id="ico-property" viewBox="0 0 28 28">
      <path d="M2 26V13h3v-3h2v3h2V7h2V3h2v4h2v6h2V9h3v4h3v-2h2v15z" fill="var(--property)"/>
    </symbol>
    <symbol id="ico-owner" viewBox="0 0 28 28">
      <circle cx="14" cy="14" r="12.5" fill="#fff" stroke="var(--owner)" stroke-width="2"/>
      <circle cx="14" cy="11" r="5" fill="var(--owner)"/>
      <path d="M5.5 23c1.5-4 5-6 8.5-6s7 2 8.5 6a12 12 0 0 1-17 0z" fill="var(--owner)"/>
    </symbol>
    <symbol id="ico-tenant" viewBox="0 0 28 28">
      <circle cx="14" cy="14" r="12.5" fill="#fff" stroke="var(--tenant)" stroke-width="2"/>
      <circle cx="14" cy="11" r="5" fill="var(--tenant)"/>
      <path d="M5.5 23c1.5-4 5-6 8.5-6s7 2 8.5 6a12 12 0 0 1-17 0z" fill="var(--tenant)"/>
    </symbol>
    <symbol id="ico-staff" viewBox="0 0 28 28">
      <circle cx="7" cy="11" r="3.6" fill="var(--staff)"/>
      <circle cx="21" cy="11" r="3.6" fill="var(--staff)"/>
      <path d="M1 22c0-4 3-6 6-6s6 2 6 6z" fill="var(--staff)"/>
      <path d="M15 22c0-4 3-6 6-6s6 2 6 6z" fill="var(--staff)"/>
      <circle cx="14" cy="10" r="4.2" fill="var(--staff)" stroke="#fff" stroke-width="1"/>
      <path d="M6.5 23c0-5 3.5-7.5 7.5-7.5s7.5 2.5 7.5 7.5z" fill="var(--staff)" stroke="#fff" stroke-width="1"/>
    </symbol>
    <symbol id="ico-magnifier" viewBox="0 0 14 14">
      <circle cx="5.5" cy="5.5" r="4.3" fill="none" stroke="#a4a4a8" stroke-width="1.3"/>
      <line x1="8.6" y1="8.6" x2="12.5" y2="12.5" stroke="#a4a4a8" stroke-width="1.3"/>
    </symbol>
    <symbol id="ico-back" viewBox="0 0 12 20">
      <path d="M10 2L2 10l8 8" fill="none" stroke="#fff" stroke-width="2.6" stroke-linecap="round" stroke-linejoin="round"/>
    </symbol>
    <symbol id="ico-chevron" viewBox="0 0 12 22">
      <path d="M1.5 1.5L10.5 11l-9 9.5" fill="none" stroke="#8e8e93" stroke-width="1.4"/>
    </symbol>
    <symbol id="ico-wifi" viewBox="0 0 14 10">
      <path d="M1 3.5a8.5 8.5 0 0 1 12 0M3 5.7a5.5 5.5 0 0 1 8 0M5 7.8a2.6 2.6 0 0 1 4 0" fill="none" stroke="#1b1b1b" stroke-width="1.3"/>
    </symbol>
    <symbol id="ico-bt" viewBox="0 0 8 12">
      <path d="M1 3.5l6 5-3 2.5V1l3 2.5-6 5" fill="none" stroke="#1b1b1b" stroke-width="1"/>
    </symbol>
    <symbol id="ico-bolt" viewBox="0 0 6 10">
      <path d="M4 0L0 6h2.5L2 10l4-6H3.5z" fill="#1b1b1b"/>
    </symbol>
    <symbol id="ico-shift" viewBox="0 0 20 18">
      <path d="M10 1.5L2 9.5h4.5V16h7V9.5H18z" fill="none" stroke="#1b1b1b" stroke-width="1.3" stroke-linejoin="round"/>
    </symbol>
    <symbol id="ico-delete" viewBox="0 0 26 18">
      <path d="M8 2h16v14H8L1.5 9z" fill="none" stroke="#1b1b1b" stroke-width="1.3" stroke-linejoin="round"/>
      <path d="M12 5.5l7 7M19 5.5l-7 7" stroke="#1b1b1b" stroke-width="1.3"/>
    </symbol>
    <symbol id="ico-globe" viewBox="0 0 20 20">
      <g fill="none" stroke="#1b1b1b" stroke-width="1.1">
        <circle cx="10" cy="10" r="8.5"/><ellipse cx="10" cy="10" rx="4" ry="8.5"/>
        <line x1="10" y1="1.5" x2="10" y2="18.5"/><line x1="1.5" y1="10" x2="18.5" y2="10"/>
        <path d="M3 5.5h14M3 14.5h14"/>
      </g>
    </symbol>
    <symbol id="ico-mic" viewBox="0 0 14 22">
      <rect x="4" y="1" width="6" height="12" rx="3" fill="none" stroke="#1b1b1b" stroke-width="1.2"/>
      <path d="M1.5 9.5a5.5 5.5 0 0 0 11 0M7 15v5M4 20.5h6" fill="none" stroke="#1b1b1b" stroke-width="1.2"/>
    </symbol>
    <symbol id="ico-clear" viewBox="0 0 16 16">
      <circle cx="8" cy="8" r="7.5" fill="#a4a4a8"/>
      <path d="M5 5l6 6M11 5l-6 6" stroke="#fff" stroke-width="1.6"/>
    </symbol>
  </defs>
</svg>

<!-- Empty search state -->
<section class="screen screen--empty" aria-label="Velorak search, empty">
  <div class="status">
    <div class="status__left">
      <span class="signal"><i></i><i></i><i></i><i class="off"></i><i class="off"></i></span>
      <span>Telvo</span>
      <svg width="14" height="10"><use href="#ico-wifi"/></svg>
    </div>
    <div class="status__time">15.45</div>
    <div class="status__right">
      <svg width="8" height="12"><use href="#ico-bt"/></svg>
      <span>5%</span><span class="battery"></span>
      <svg width="6" height="10"><use href="#ico-bolt"/></svg>
    </div>
  </div>
  <header class="nav">
    <div class="nav__back"><svg width="12" height="20"><use href="#ico-back"/></svg>Home</div>
    <h1 class="nav__title">Search</h1>
  </header>
  <nav class="tabs">
    <div class="tab tab--active"><svg><use href="#ico-portfolio"/></svg>My Portfolio</div>
    <div class="tab"><svg><use href="#ico-property"/></svg>Property</div>
    <div class="tab"><svg><use href="#ico-owner"/></svg>Owner</div>
    <div class="tab"><svg><use href="#ico-tenant"/></svg>Tenant</div>
    <div class="tab"><svg><use href="#ico-staff"/></svg>Staff</div>
  </nav>
  <div class="search">
    <div class="search__field"><svg width="14" height="14"><use href="#ico-magnifier"/></svg>Search</div>
  </div>
  <div class="results">
    <div class="row"></div><div class="row"></div><div class="row"></div><div class="row"></div>
  </div>
  <div class="keyboard">
    <div class="keys"><span class="key">Q</span><span class="key">W</span><span class="key">E</span><span class="key">R</span><span class="key">T</span><span class="key">Y</span><span class="key">U</span><span class="key">I</span><span class="key">O</span><span class="key">P</span></div>
    <div class="keys keys--home"><span class="key">A</span><span class="key">S</span><span class="key">D</span><span class="key">F</span><span class="key">G</span><span class="key">H</span><span class="key">J</span><span class="key">K</span><span class="key">L</span></div>
    <div class="keys keys--shift">
      <span class="key key--special key--wide"><svg width="20" height="18"><use href="#ico-shift"/></svg></span>
      <span class="group"><span class="key">Z</span><span class="key">X</span><span class="key">C</span><span class="key">V</span><span class="key">B</span><span class="key">N</span><span class="key">M</span></span>
      <span class="key key--special key--wide"><svg width="26" height="18"><use href="#ico-delete"/></svg></span>
    </div>
    <div class="keys keys--bottom">
      <span class="key key--special key--num">123</span>
      <span class="key key--special key--globe"><svg width="20" height="20"><use href="#ico-globe"/></svg></span>
      <span class="key key--mic"><svg width="14" height="22"><use href="#ico-mic"/></svg></span>
      <span class="key key--space">space</span>
      <span class="key key--com">.com</span>
      <span class="key key--go">Go</span>
    </div>
  </div>
</section>

<!-- Results state -->
<section class="screen screen--results" aria-label="Velorak search, results">
  <div class="status">
    <div class="status__left">
      <span class="signal"><i></i><i></i><i></i><i class="off"></i><i class="off"></i></span>
      <span>Telvo</span>
      <svg width="14" height="10"><use href="#ico-wifi"/></svg>
    </div>
    <div class="status__time">15.45</div>
    <div class="status__right">
      <svg width="8" height="12"><use href="#ico-bt"/></svg>
      <span>5%</span><span class="battery"></span>
      <svg width="6" height="10"><use href="#ico-bolt"/></svg>
    </div>
  </div>
  <header class="nav">
    <div class="nav__back"><svg width="12" height="20"><use href="#ico-back"/></svg>Home</div>
    <h1 class="nav__title">Search</h1>
  </header>
  <nav class="tabs">
    <div class="tab tab--active"><svg><use href="#ico-portfolio"/></svg>My Portfolio</div>
    <div class="tab"><svg><use href="#ico-property"/></svg>Property</div>
    <div class="tab"><svg><use href="#ico-owner"/></svg>Owner</div>
    <div class="tab"><svg><use href="#ico-tenant"/></svg>Tenant</div>
    <div class="tab"><svg><use href="#ico-staff"/></svg>Staff</div>
  </nav>
  <div class="search">
    <div class="search__field"><svg width="14" height="14"><use href="#ico-magnifier"/></svg>Main<svg class="clear" width="15" height="15"><use href="#ico-clear"/></svg></div>
  </div>
  <div class="results">
    <div class="row"><svg class="row__icon"><use href="#ico-property"/></svg><span class="row__text">2/9 Mainsbury St<br>HARLOW EAST NSW 2098</span><svg class="row__chevron" width="12" height="22"><use href="#ico-chevron"/></svg></div>
    <div class="row"><svg class="row__icon"><use href="#ico-property"/></svg><span class="row__text">Tallis 604/22 Sir Mainard Young<br>Crescent</span><svg class="row__chevron" width="12" height="22"><use href="#ico-chevron"/></svg></div>
    <div class="row"><svg class="row__icon"><use href="#ico-owner"/></svg><span class="row__text">Clara Winslow Trustee For KTR<br>Maintenance</span><svg class="row__chevron" width="12" height="22"><use href="#ico-chevron"/></svg></div>
    <div class="row"><svg class="row__icon"><use href="#ico-tenant"/></svg><span class="row__text">Mainor, Devan Ashok</span><svg class="row__chevron" width="12" height="22"><use href="#ico-chevron"/></svg></div>
  </div>
  <div class="keyboard">
    <div class="keys"><span class="key">Q</span><span class="key">W</span><span class="key">E</span><span class="key">R</span><span class="key">T</span><span class="key">Y</span><span class="key">U</span><span class="key">I</span><span class="key">O</span><span class="key">P</span></div>
    <div class="keys keys--home"><span class="key">A</span><span class="key">S</span><span class="key">D</span><span class="key">F</span><span class="key">G</span><span class="key">H</span><span class="key">J</span><span class="key">K</span><span class="key">L</span></div>
    <div class="keys keys--shift">
      <span class="key key--special key--wide"><svg width="20" height="18"><use href="#ico-shift"/></svg></span>
      <span class="group"><span class="key">Z</span><span class="key">X</span><span class="key">C</span><span class="key">V</span><span class="key">B</span><span class="key">N</span><span class="key">M</span></span>
      <span class="key key--special key--wide"><svg width="26" height="18"><use href="#ico-delete"/></svg></span>
    </div>
    <div class="keys keys--bottom">
      <span class="key key--special key--num">123</span>
      <span class="key key--special key--globe"><svg width="20" height="20"><use href="#ico-globe"/></svg></span>
      <span class="key key--mic"><svg width="14" height="22"><use href="#ico-mic"/></svg></span>
      <span class="key key--space">space</span>
      <span class="key key--com">.com</span>
      <span class="key key--go">Go</span>
    </div>
  </div>
</section>

</body>
</html>
```